Digital Signage Slide Design – Celebrations

I am looking for a digital designer for the design of our Celebration slide for our Digital Signage solution. I have attached two basic designs (landscape & portrait) of our current celebration slide. We are wanting a completely new look and feel that delivers an inspiring layout. Your goals is to provide a design that will grab peoples attention through design and content placement. Note: the final production of the slide will have animated transitioning effects. What we require from you is the design (in PSD format) for both a Landscape (1920 x 1080) and Portrait (1080 x 1920) oriented screen and a written description of how you see the animation working.If you prefer, you can use your own mock-up content and images. What we have supplied in the example mock-up, is only example content.Please refer to the following link to view an example of what a final animated slide looks like - https://www.clipvantor.example/watch?v=QmTb83kLw57 If you are unsure of what a Digital Signage is, please refer to the following page on our website - https://www.brightpanelo.example/industry/corporate-culture
Target Market(s)
Internal Communication Channel for Large Organisations
Colors
Designer to choose colors to be used in the design.
Look and feel
Each slider illustrates characteristics of the customer's brand and the style your logo design should communicate.

```html
<!DOCTYPE html>
<html lang="en">
<head>
<meta charset="utf-8">
<title>Work Anniversary – Marcus Hale</title>
<link rel="stylesheet" href="https://fonts.googleapis.com/css2?family=Montserrat:wght@300;400;600;700&family=Catamaran:wght@400;500&display=swap">
<style>
  :root {
    --white: #ffffff;
    --navy: #0b1c36;
    --navy-band: rgba(9, 24, 48, 0.88);
    --ink: #1d2a3d;
    --steel: #8fa3b2;
    --teal: #2f8fc0;
    --deep-blue: #0d3f66;
    --warm-dark: #3a2c22;
    --warm-mid: #7a5a3e;
    --shirt: #c9d4e2;
  }
  html, body {
    margin: 0;
    padding: 0;
    width: 1200px;
    height: 675px;
    overflow: hidden;
    background: #111;
  }
  .slide {
    position: relative;
    width: 1200px;
    height: 675px;
    overflow: hidden;
    font-family: "Montserrat", sans-serif;
    color: var(--white);
  }
  .portrait-photo {
    position: absolute;
    inset: 0;
    background:
      radial-gradient(ellipse 260px 340px at 880px 430px, rgba(30, 40, 60, 0.9), transparent 70%),
      radial-gradient(circle at 1060px 300px, #b9772f 0, transparent 22%),
      linear-gradient(90deg, var(--warm-dark) 0%, var(--warm-mid) 60%, #4a3a2e 100%);
  }
  .topo-texture {
    position: absolute;
    left: 0;
    top: 0;
    width: 760px;
    height: 675px;
    background:
      linear-gradient(90deg, rgba(0,0,0,0) 70%, rgba(0,0,0,0) 100%),
      linear-gradient(180deg, #b9c4cb 0%, #8aa0ae 22%, #3f7fa8 45%, var(--teal) 65%, var(--deep-blue) 100%);
    -webkit-mask-image: linear-gradient(90deg, #000 72%, transparent 100%);
            mask-image: linear-gradient(90deg, #000 72%, transparent 100%);
  }
  .name-band {
    position: absolute;
    left: 0;
    top: 173px;
    width: 689px;
    height: 136px;
    background: var(--navy-band);
    border-radius: 0 68px 68px 0;
  }
  .headline {
    position: absolute;
    left: 56px;
    top: 76px;
    margin: 0;
    font-size: 64px;
    font-weight: 600;
    letter-spacing: -1px;
    line-height: 1;
  }
  .employee-name {
    position: absolute;
    left: 122px;
    top: 186px;
    margin: 0;
    font-size: 64px;
    line-height: 1;
    letter-spacing: -0.5px;
    font-weight: 600;
  }
  .employee-name .surname { font-weight: 300; }
  .anniversary-date {
    position: absolute;
    right: 553px;
    top: 256px;
    margin: 0;
    font-size: 36px;
    line-height: 1;
    font-weight: 700;
  }
  .anniversary-date .day { font-weight: 400; }
  .congrats {
    position: absolute;
    left: 122px;
    top: 334px;
    margin: 0;
    font-family: "Catamaran", sans-serif;
    font-size: 46px;
    font-weight: 500;
    line-height: 1;
  }
  .service-pill {
    position: absolute;
    left: 103px;
    top: 392px;
    width: 425px;
    height: 66px;
    background: var(--white);
    border-radius: 33px;
    display: flex;
    align-items: center;
    color: var(--ink);
    font-family: "Catamaran", sans-serif;
  }
  .service-years {
    width: 72px;
    height: 56px;
    margin-left: 6px;
    border: 3px solid var(--navy);
    border-radius: 30px;
    box-sizing: border-box;
    display: flex;
    align-items: center;
    justify-content: center;
    font-size: 40px;
    font-weight: 500;
  }
  .service-text {
    margin-left: 16px;
    font-size: 30px;
    padding-top: 6px;
  }
  .thanks {
    position: absolute;
    left: 122px;
    top: 490px;
    margin: 0;
    font-family: "Catamaran", sans-serif;
    line-height: 1;
  }
  .thanks-lead {
    display: block;
    font-size: 52px;
    font-weight: 500;
  }
  .thanks-team {
    display: block;
    font-size: 42px;
    font-weight: 400;
    margin-top: 2px;
  }
</style>
</head>
<body>
<main class="slide">
  <div class="portrait-photo" role="img" aria-label="Portrait photo of the employee in glasses, shirt, tie and waistcoat, against a blurred warm building backdrop"></div>
  <div class="topo-texture" role="img" aria-label="Decorative topographic contour-line texture in grey and blue"></div>
  <div class="name-band"></div>

  <h1 class="headline">WORK ANNIVERSARY</h1>
  <h2 class="employee-name">MARCUS<span class="surname">HALE</span></h2>
  <p class="anniversary-date">SEPTEMBER<span class="day">10</span></p>

  <p class="congrats">Congratulations on</p>
  <div class="service-pill">
    <span class="service-years">5</span>
    <span class="service-text">years dedicated service.</span>
  </div>

  <p class="thanks">
    <span class="thanks-lead">THANK YOU</span>
    <span class="thanks-team">from all your team!</span>
  </p>
</main>
</body>
</html>
```